Frostvale Cold Packs needs stationery designed for their new logo

We have a new logo so now want all our stationery to be redesigned.
Frostvale is a gel ice pack product used by the seafood & food industry to transport chilled products around the world.

We would like to use our new logo with icy or snow backgrounds or elements.
Our company tag line is "Keep your products chilled for longer"
I'll attach our old business cards so that you can use the text off them.
2nd attachment is our new logo to be used.

We want a design for:
- Business cards
- Letter Head
- Email signature

Target Market(s)

seafood & chilled food distributors

Industry/Entity Type

Industry

Font styles to use
Sans Serif

Colors
0492cd
85cae6
cee9f5

Requirements
Must have
• Our logo
Nice to have
• Snow or ice background or image incorporated somehow

```html
<!DOCTYPE html>
<html lang="en">
<head>
<meta charset="utf-8">
<title>Frostvale Cold Packs – Stationery</title>
<link rel="stylesheet" href="https://fonts.googleapis.com/css2?family=Source+Sans+3:wght@400;600&family=Tinos&display=swap">
<style>
:root{
  --board:#a3a1a2;
  --paper:#f6f5f3;
  --white:#ffffff;
  --blue:#0474c8;
  --ink:#4a4a4a;
  --muted:#8c8c8c;
  --swoosh-grey:#8e8e90;
  --shadow:0 3px 8px rgba(0,0,0,.35);
}
*{margin:0;padding:0;box-sizing:border-box}
html,body{width:1200px;height:890px;overflow:hidden;background:var(--board)}
body{position:relative;font-family:"Source Sans 3",sans-serif;color:var(--ink)}
.piece{position:absolute;background:var(--white);box-shadow:var(--shadow);overflow:hidden}
.piece.gradient{background:linear-gradient(90deg,#e9e9ea 0%,#ffffff 45%,#f0f0f1 100%)}
.swoosh{position:absolute;left:0;bottom:0;width:100%;display:block}
.brand{position:absolute;display:flex;align-items:center;gap:5px;color:#7b7b7d;font-weight:600;white-space:nowrap;letter-spacing:-.2px}
.brand .dot{border-radius:50%;background:var(--blue);flex:none}
.name{color:var(--blue);font-weight:600}
.role{color:var(--muted)}
.city{font-weight:600;text-transform:uppercase}
.block{position:absolute;line-height:1.25}
.contact-row{display:flex;align-items:center;gap:3px}
.icon{width:7px;height:7px;flex:none}
.divider{position:absolute;width:1px;background:#c9c9c9}
.label{position:absolute;font-family:"Tinos",serif;font-size:12px;color:#f2f2f2;transform:translateX(-50%);white-space:nowrap}

/* letterhead */
.letterhead{left:47px;top:38px;width:578px;height:816px;background:var(--paper)}
.letterhead .brand{left:42px;top:58px;font-size:24px}
.letterhead .brand .dot{width:18px;height:18px}
.letterhead .header-contact{right:60px;top:36px;text-align:right;font-size:9.5px}
.letterhead .header-contact p{margin-bottom:3px}
.letterhead .contact-row{justify-content:flex-end;gap:5px}

/* business card back */
.card-back{left:911px;top:707px;width:253px;height:144px;background:var(--blue);color:var(--white);text-align:center}
.card-back .brand-large{position:absolute;left:0;right:0;top:40px;font-size:26px;font-weight:600}
.card-back .tagline{position:absolute;left:0;right:0;bottom:14px;font-size:7px;font-style:italic}
</style>
</head>
<body>

<!-- Letterhead -->
<section class="piece letterhead" aria-label="Letterhead">
  <div class="brand"><span class="dot"></span>Frostvale</div>
  <div class="block header-contact">
    <p><span class="city">Sydney :</span> 14 Harbour Lane<br>North Sydney, NSW 2060</p>
    <p><span class="city">Auckland :</span> 5 Kowhai Road<br>Silverdale, Auckland 0932</p>
    <div class="contact-row">owen.hartley@frostvale.com.au
      <svg class="icon" viewBox="0 0 10 10"><rect x="0" y="2" width="10" height="6.5" fill="#0474c8"/><path d="M0 2 L5 6 L10 2" stroke="#fff" fill="none"/></svg></div>
    <div class="contact-row">www.frostvale.com.au
      <svg class="icon" viewBox="0 0 10 10"><circle cx="5" cy="5" r="5" fill="#0474c8"/><path d="M2 5h6M5 1v8" stroke="#fff" stroke-width=".9"/></svg></div>
  </div>
  <svg class="swoosh" viewBox="0 0 578 50" height="50" preserveAspectRatio="none">
    <path d="M0 0 Q250 32 578 10 L578 50 L0 50Z" fill="var(--swoosh-grey)"/>
    <path d="M0 9 Q250 38 578 14 L578 50 L0 50Z" fill="#fff"/>
    <path d="M0 12 Q250 40 578 17 L578 50 L0 50Z" fill="var(--blue)"/>
  </svg>
</section>

<!-- Email signature 02 -->
<section class="piece gradient" style="left:657px;top:338px;width:316px;height:152px" aria-label="Email signature 02">
  <div class="brand" style="left:22px;top:58px;font-size:15px"><span class="dot" style="width:12px;height:12px"></span>Frostvale</div>
  <div class="divider" style="left:151px;top:14px;height:110px"></div>
  <div class="block" style="left:159px;top:12px;font-size:7.5px">
    <div class="name" style="font-size:11.5px">Owen Hartley</div>
    <div class="role" style="margin-bottom:6px">Business Development</div>
    <div class="city">Sydney</div><div>14 Harbour Lane<br>North Sydney, NSW 2060</div>
    <div class="city" style="margin-top:3px">Auckland</div><div style="margin-bottom:6px">5 Kowhai Road, Silverdale<br>Auckland 0932</div>
    <div class="contact-row"><svg class="icon" viewBox="0 0 10 10"><rect y="2" width="10" height="6.5" fill="#0474c8"/></svg>owen.hartley@frostvale.com.au</div>
    <div class="contact-row"><svg class="icon" viewBox="0 0 10 10"><circle cx="5" cy="5" r="5" fill="#0474c8"/></svg>www.frostvale.com.au</div>
  </div>
  <svg class="swoosh" viewBox="0 0 316 26" height="26" preserveAspectRatio="none">
    <path d="M0 0 Q140 16 316 8 L316 26 L0 26Z" fill="var(--swoosh-grey)"/>
    <path d="M0 5 Q140 19 316 11 L316 26 L0 26Z" fill="#fff"/>
    <path d="M0 7 Q140 21 316 13 L316 26 L0 26Z" fill="var(--blue)"/>
  </svg>
</section>
<div class="label" style="left:805px;top:494px">Email Signature_02</div>

<!-- Email signature 03 -->
<section class="piece gradient" style="left:994px;top:279px;width:167px;height:212px" aria-label="Email signature 03">
  <div class="brand" style="left:19px;top:23px;font-size:15px"><span class="dot" style="width:12px;height:12px"></span>Frostvale</div>
  <div class="block" style="left:19px;top:59px;font-size:7.5px">
    <div class="name" style="font-size:11.5px">Owen Hartley</div>
    <div class="role" style="margin-bottom:6px">Business Development</div>
    <div class="city">Sydney</div><div>14 Harbour Lane<br>North Sydney, NSW 2060</div>
    <div class="city" style="margin-top:3px">Auckland</div><div style="margin-bottom:6px">5 Kowhai Road, Silverdale<br>Auckland 0932</div>
    <div class="contact-row"><svg class="icon" viewBox="0 0 10 10"><rect y="2" width="10" height="6.5" fill="#0474c8"/></svg>owen.hartley@frostvale.com.au</div>
    <div class="contact-row"><svg class="icon" viewBox="0 0 10 10"><circle cx="5" cy="5" r="5" fill="#0474c8"/></svg>www.frostvale.com.au</div>
  </div>
  <svg class="swoosh" viewBox="0 0 167 18" height="18" preserveAspectRatio="none">
    <path d="M0 0 Q70 12 167 6 L167 18 L0 18Z" fill="var(--swoosh-grey)"/>
    <path d="M0 4 Q70 14 167 8 L167 18 L0 18Z" fill="#fff"/>
    <path d="M0 6 Q70 16 167 10 L167 18 L0 18Z" fill="var(--blue)"/>
  </svg>
</section>
<div class="label" style="left:1086px;top:499px">Email Signature_03</div>

<!-- Email signature 01 -->
<section class="piece gradient" style="left:665px;top:537px;width:491px;height:126px" aria-label="Email signature 01">
  <div class="brand" style="left:30px;top:47px;font-size:15px"><span class="dot" style="width:12px;height:12px"></span>Frostvale</div>
  <div class="divider" style="left:179px;top:25px;height:60px"></div>
  <div class="block" style="left:190px;top:30px;width:160px;text-align:center;font-size:7.5px">
    <div class="name" style="font-size:11.5px">Owen Hartley</div>
    <div class="role" style="margin-bottom:6px">Business Development</div>
    <div>owen.hartley@frostvale.com.au</div>
    <div>www.frostvale.com.au</div>
  </div>
  <div class="divider" style="left:353px;top:25px;height:60px"></div>
  <div class="block" style="left:370px;top:26px;font-size:7.5px">
    <div class="city">Sydney</div><div>14 Harbour Lane<br>North Sydney, NSW 2060</div>
    <div class="city" style="margin-top:6px">Auckland</div><div>5 Kowhai Road, Silverdale<br>Auckland 0932</div>
  </div>
  <svg class="swoosh" viewBox="0 0 491 34" height="34" preserveAspectRatio="none">
    <path d="M0 0 Q220 28 491 9 L491 34 L0 34Z" fill="var(--swoosh-grey)"/>
    <path d="M0 7 Q220 32 491 12 L491 34 L0 34Z" fill="#fff"/>
    <path d="M0 9 Q220 34 491 14 L491 34 L0 34Z" fill="var(--blue)"/>
  </svg>
</section>
<div class="label" style="left:913px;top:672px">Email Signature_01</div>

<!-- Business card front -->
<section class="piece" style="left:644px;top:706px;width:254px;height:145px" aria-label="Business card front">
  <div class="brand" style="left:10px;top:61px;font-size:13px"><span class="dot" style="width:10px;height:10px"></span>Frostvale</div>
  <div class="block" style="left:127px;top:20px;font-size:6.3px">
    <div class="name" style="font-size:9.5px">Owen Hartley</div>
    <div class="role" style="margin-bottom:5px">Business Development</div>
    <div class="city">Sydney</div><div>14 Harbour Lane<br>North Sydney, NSW 2060</div>
    <div class="city" style="margin-top:3px">Auckland</div><div style="margin-bottom:4px">5 Kowhai Road, Silverdale<br>Auckland 0932</div>
    <div class="contact-row"><svg class="icon" style="width:6px;height:6px" viewBox="0 0 10 10"><rect y="2" width="10" height="6.5" fill="#0474c8"/></svg>owen.hartley@frostvale.com.au</div>
    <div class="contact-row"><svg class="icon" style="width:6px;height:6px" viewBox="0 0 10 10"><circle cx="5" cy="5" r="5" fill="#0474c8"/></svg>www.frostvale.com.au</div>
  </div>
  <svg class="swoosh" viewBox="0 0 254 22" height="22" preserveAspectRatio="none">
    <path d="M0 0 Q110 16 254 6 L254 22 L0 22Z" fill="var(--swoosh-grey)"/>
    <path d="M0 5 Q110 19 254 9 L254 22 L0 22Z" fill="#fff"/>
    <path d="M0 7 Q110 21 254 11 L254 22 L0 22Z" fill="var(--blue)"/>
  </svg>
</section>

<!-- Business card back -->
<section class="piece card-back" aria-label="Business card back">
  <div class="brand-large">Frostvale</div>
  <div class="tagline">Keep your products chilled for longer</div>
</section>

</body>
</html>
```